Pelican Litigation Funding Letterhead & Document Template

We need a letter head designed for our fund. Our fund works with law firms and investors across the globe. We need a a cover letter template as well as a document template for subsequent pages. Blue and white color scheme is preferred. This is our predecessor's website: https://www.pelicanvq.com/index.html. Please see our logo attached. The logo color code is #19478d. Font is Gotham-Medium.
Target Market(s)
Sophisticated investors and law firms
Font styles to use
Sans Serif
Colors
0255a3

```html
<!DOCTYPE html>
<html lang="en">
<head>
<meta charset="utf-8">
<title>Pelican Litigation Funding – Letterhead</title>
<link href="https://fonts.googleapis.com/css2?family=Montserrat:wght@500;600&family=Poppins:wght@400;500&family=Tinos&display=swap" rel="stylesheet">
<style>
  :root {
    --brand: #19478d;
    --brand-deep: #0255a3;
    --accent: #3a8fd0;
    --ink: #24427c;
    --backdrop: #e6e7e9;
    --paper: #ffffff;
  }
  * { box-sizing: border-box; margin: 0; padding: 0; }
  html, body { width: 1200px; height: 800px; overflow: hidden; }
  body {
    background: var(--backdrop);
    display: flex; align-items: center; justify-content: center;
    font-family: "Poppins", sans-serif; color: var(--ink);
  }
  .letterhead {
    position: relative; width: 540px; height: 764px;
    background: var(--paper);
    box-shadow: 0 2px 8px rgba(0,0,0,.12);
  }
  .brand {
    position: absolute; left: 48px; top: 48px;
    display: flex; align-items: center; gap: 8px;
    font-family: "Montserrat", sans-serif; font-weight: 600;
    font-size: 11px; letter-spacing: .06em; text-transform: uppercase;
    color: var(--brand);
  }
  .brand__square { width: 12px; height: 12px; background: var(--brand); }
  .contact {
    position: absolute; right: 34px; top: 96px;
    font-size: 7.5px; line-height: 1.45; color: var(--brand);
  }
  .contact li { list-style: none; display: flex; gap: 6px; align-items: flex-start; }
  .contact svg { width: 7px; height: 7px; margin-top: 2px; flex: none; fill: var(--brand); }
  .contact .plain { padding-left: 13px; }
  .edge-bar {
    position: absolute; right: 0; top: 140px; width: 9px; height: 62px;
    background: var(--brand);
  }
  .recipient { position: absolute; left: 48px; top: 160px; font-size: 8px; line-height: 1.55; }
  .recipient__date { margin-bottom: 10px; }
  .recipient__name { color: var(--accent); font-weight: 500; font-size: 10px; }
  .salutation {
    position: absolute; left: 0; right: 0; top: 268px; text-align: center;
    font-family: "Montserrat", sans-serif; font-weight: 600; font-size: 11px;
    letter-spacing: .08em; color: var(--brand);
  }
  .body-copy { position: absolute; left: 48px; right: 48px; top: 300px; font-size: 8px; line-height: 1.6; }
  .body-copy p + p { margin-top: 14px; }
  .signoff {
    position: absolute; right: 56px; top: 590px; width: 110px; text-align: center;
    font-family: "Tinos", serif;
  }
  .signoff__mark { display: block; width: 48px; height: 28px; margin: 0 auto 6px; background: #dfe5f0; border-radius: 4px; }
  .signoff__name { font-size: 11px; color: var(--ink); }
  .signoff__role { font-size: 8px; color: var(--accent); }
  .web-band {
    position: absolute; left: 0; top: 680px; width: 196px; height: 22px;
    background: var(--brand);
    color: #fff; font-family: "Montserrat", sans-serif; font-weight: 500;
    font-size: 9px; letter-spacing: .06em; line-height: 22px; padding-left: 38px;
  }
  .footer-square { position: absolute; right: 52px; bottom: 36px; width: 14px; height: 14px; background: var(--brand); }
</style>
</head>
<body>
  <article class="letterhead">
    <div class="brand"><span class="brand__square"></span>Pelican Litigation Funding</div>

    <ul class="contact">
      <li><svg viewBox="0 0 10 10"><path d="M2 0h2l1 3-1.5 1a6 6 0 0 0 2.5 2.5L7 5l3 1v2c0 1-1 2-2 2A8 8 0 0 1 0 2c0-1 1-2 2-2z"/></svg>(555) 204-7188</li>
      <li><svg viewBox="0 0 10 10"><rect x="1" y="2" width="8" height="7" rx="1"/></svg>(555) 204-7190</li>
      <li><svg viewBox="0 0 10 10"><rect x="0" y="2" width="10" height="6" rx="1"/></svg>info@pelicanvq.com</li>
      <li><svg viewBox="0 0 10 10"><path d="M5 0a3.5 3.5 0 0 1 3.5 3.5C8.5 6 5 10 5 10S1.5 6 1.5 3.5A3.5 3.5 0 0 1 5 0z"/></svg>Linden Court – Top Floor</li>
      <li class="plain">410 Marlow Ave, Suite 900</li>
      <li class="plain">Austin, Texas 78701</li>
    </ul>
    <div class="edge-bar"></div>

    <div class="recipient">
      <p class="recipient__date">Wednesday, October 28, 2020</p>
      <p class="recipient__name">Mara Ellison</p>
      <p>18 Harlow Ridge Lane</p>
      <p>7 Bexley Street</p>
      <p>Columbus Ohio 43085</p>
    </div>

    <h1 class="salutation">DEAR MARA</h1>

    <div class="body-copy">
      <p>Lorem ipsum dolor sit amet, cetero accusamus intellegat at his, usu aeterno erroribus sadipscing id, nam virtute equidem reprimique ea. Est cu modo oblique theophrastus, vix ex ferri dicam iisque, idque nostrud eam ut. Tation constituto repriique ut vis. Cu appareat dissentias qui. Vitae causae ceteros mea an, pro mutat admodum ex, ad quo commodo principes. Eam ignota impetus epicuri no, augue affert in vis. Pro nobis veteem eu, ex ius alia utamur explicari.</p>
      <p>Lorem ipsum dolor sit amet, cetero accusamus intellegat at his, usu aeterno erroribus sadipscing id, nam virtute equidem reprimique ea. Est cu modo oblique theophrastus, vix ex ferri dicam iisque, idque nostrud eam ut. Tation constituto repriique ut vis. Cu appareat dissentias qui.</p>
      <p>Tation constituto reprimique ut vis. Cu appareat dissentias qui. Vitae causae ceteros mea an, pro mutat admodum ex, ad quo commodo principes. Eam ignota impetus epicuri no.</p>
    </div>

    <div class="signoff">
      <span class="signoff__mark" role="img" aria-label="Handwritten signature"></span>
      <p class="signoff__name">Enter Your Name</p>
      <p class="signoff__role">Lawyer</p>
    </div>

    <div class="web-band">WWW.PELICANVQ.COM</div>
    <div class="footer-square"></div>
  </article>
</body>
</html>
```